VORN - Business cards

Business card to be created for Commercial sales staff

Target Market(s)

Commercial businesses

Industry/Entity Type

Commercial

Contact Information for Business Card

Look professional. For commercial clients

Colors
ffffff

Requirements
Must have
• - Vorn Logo
• - Commercial sales staff as postion
• - room for commerical sales manager role
• - person name and their mobile number
• - Website : vornelectrical.com.au
Nice to have
• White background.
• On back of business card just have the logo no other information
Should not have
• Should only have white background on front of card.

```html
<!DOCTYPE html>
<html lang="en">
<head>
<meta charset="utf-8">
<title>VORN – Business cards</title>
<link href="https://fonts.googleapis.com/css2?family=Open+Sans:wght@400;600;700;800&display=swap" rel="stylesheet">
<style>
  :root {
    --page: #2b2b2b;
    --card: #ffffff;
    --red: #c8101a;
    --ink: #1a1a1a;
    --muted: #555555;
  }
  * { box-sizing: border-box; margin: 0; padding: 0; }
  html, body { width: 1200px; height: 882px; overflow: hidden; }
  body {
    background: var(--page);
    font-family: "Open Sans", Arial, sans-serif;
    position: relative;
  }
  .card {
    position: absolute;
    width: 600px;
    height: 343px;
    background: var(--card);
    overflow: hidden;
    box-shadow: 0 10px 30px rgba(0,0,0,.45);
  }
  .card-back { left: 300px; top: 40px; }
  .card-front { left: 300px; top: 423px; }
  .card .shapes { position: absolute; inset: 0; width: 100%; height: 100%; }

  .brand { position: absolute; display: flex; align-items: center; gap: 12px; }
  .brand-mark {
    width: 54px; height: 54px; border-radius: 50%;
    background: var(--red);
  }
  .brand-name {
    font-weight: 800; color: var(--ink);
    letter-spacing: 1px; line-height: 1;
  }
  .card-back .brand { left: 150px; top: 128px; }
  .card-back .brand-name { font-size: 68px; }
  .card-back .brand-mark { width: 66px; height: 66px; }
  .card-front .brand { left: 40px; top: 76px; }
  .card-front .brand-name { font-size: 52px; }

  .person { position: absolute; right: 70px; top: 58px; text-align: right; }
  .person-name { color: var(--red); font-weight: 700; font-size: 19px; }
  .person-role {
    color: var(--ink); font-weight: 600; font-size: 13px;
    letter-spacing: 4px; margin-top: 6px;
  }

  .contacts {
    position: absolute; left: 46px; top: 205px;
    list-style: none; font-size: 14px; color: var(--muted);
  }
  .contacts li { display: flex; align-items: center; gap: 14px; height: 22px; letter-spacing: .6px; }
  .contacts svg { width: 12px; height: 12px; fill: var(--red); flex: none; }

  .address {
    position: absolute; left: 290px; top: 286px;
    display: flex; align-items: center; gap: 8px;
    color: #fff; font-size: 14px;
  }
  .address svg { width: 12px; height: 16px; fill: #fff; }
</style>
</head>
<body>

<section class="card card-back" aria-label="Card back">
  <svg class="shapes" viewBox="0 0 600 343" preserveAspectRatio="none" aria-hidden="true">
    <polygon points="0,318 600,250 600,268 0,343" fill="var(--red)"/>
  </svg>
  <div class="brand">
    <span class="brand-mark"></span>
    <span class="brand-name">VORN</span>
  </div>
</section>

<section class="card card-front" aria-label="Card front">
  <svg class="shapes" viewBox="0 0 600 343" preserveAspectRatio="none" aria-hidden="true">
    <polygon points="548,0 600,0 600,300 555,300 555,80 530,62 548,50" fill="var(--red)"/>
    <polygon points="270,272 600,272 600,318 245,318" fill="var(--red)"/>
  </svg>

  <div class="brand">
    <span class="brand-mark"></span>
    <span class="brand-name">VORN</span>
  </div>

  <div class="person">
    <p class="person-name">PERSONS NAME</p>
    <p class="person-role">POSITION</p>
  </div>

  <ul class="contacts">
    <li>
      <svg viewBox="0 0 24 24"><path d="M6.6 10.8a15 15 0 0 0 6.6 6.6l2.2-2.2c.3-.3.7-.4 1-.2 1.1.4 2.3.6 3.6.6.6 0 1 .4 1 1V20c0 .6-.4 1-1 1A17 17 0 0 1 3 4c0-.6.4-1 1-1h3.5c.6 0 1 .4 1 1 0 1.3.2 2.5.6 3.6.1.3 0 .7-.2 1z"/></svg>
      <span>(555) 014-2290</span>
    </li>
    <li>
      <svg viewBox="0 0 24 24"><path d="M2 5h20v14H2z M2 5l10 8 10-8" /></svg>
      <span>vornelectrical.com.au</span>
    </li>
    <li>
      <svg viewBox="0 0 24 24"><circle cx="12" cy="12" r="10"/></svg>
      <span>www.vornsssssssssss.com</span>
    </li>
  </ul>

  <p class="address">
    <svg viewBox="0 0 12 16"><path d="M6 0a6 6 0 0 0-6 6c0 4.5 6 10 6 10s6-5.5 6-10a6 6 0 0 0-6-6zm0 8.5A2.5 2.5 0 1 1 6 3.5a2.5 2.5 0 0 1 0 5z"/></svg>
    <span>City, State Name, 77 Street Name str.</span>
  </p>
</section>

</body>
</html>
```